Music video company site re-design :-)

Hi guys,

I run a small music video production company called "Northgate Clip Works".

It's the new year and I'm hoping to update our website design, but am at a bit of a loss - which is where I'm desperately hoping you can help!

I need something cool and contemporary but not utterly terrifying/confusing that your average band manager/solo artist funding their own music video for the first time, won't be put off.

If you can check out our current website (http://www.NorthgateClipWorks.example) I think that would probably help :-)

Target Market(s)

Solo music artists and managers of small groups/bands.

Industry/Entity Type

It Company

Requirements
Must have
• Clear, cool but accessible.

I'll need to be able to embed Pixora videos from our Pixora-plus account into the pages...

http://www.pixora.example/framehousefilms

I'd also like to be able to optimise the site for search engines, so we'll need text and not images with text in them.

I'd also like to include or use images from our videos throughout the site, so if you can include as many of these as possible that would be great.

I've uploaded a zip file with them in, how they are used is up to you guys, but the more the merrier.
Should not have
• Images of cameras, lights, clapper boards etc...

No bloody Times New Roman unless you are really reinventing that wheel or trying to make it look like my nan made my website with clip art.

Also, no god damn emoticons ;-)

```html
<!DOCTYPE html>
<html lang="en">
<head>
<meta charset="utf-8">
<title>Northgate Clip Works</title>
<link rel="stylesheet" href="https://fonts.googleapis.com/css2?family=Montserrat:wght@600&family=Indie+Flower&family=Open+Sans:wght@400;700&family=Noto+Serif:ital,wght@1,400;1,700&display=swap">
<style>
:root{
  --bg-red:#c41e22;
  --bg-red-dark:#9e1418;
  --page:#ffffff;
  --ink:#333333;
  --ink-soft:#555555;
  --brand:#c0242a;
  --link-red:#cc1f27;
  --link-blue:#1a8ad4;
  --link-navy:#1d4fa0;
  --social:#2d6fb0;
  --rule:#2a2a2a;
  --footer:#242424;
  --footer-text:#d8d8d8;
}
*{margin:0;padding:0;box-sizing:border-box}
html,body{width:1200px;height:1080px;overflow:hidden}
body{background:linear-gradient(90deg,var(--bg-red-dark) 0,var(--bg-red) 60px,var(--bg-red) 1140px,var(--bg-red-dark) 1200px);font-family:"Open Sans",Arial,sans-serif;color:var(--ink);position:relative}
.page{position:absolute;left:120px;top:0;width:960px;height:1080px;background:var(--page);box-shadow:0 0 18px rgba(0,0,0,.45);overflow:hidden}
.rainbow{position:absolute;left:0;top:0;width:960px;height:5px;background:repeating-linear-gradient(90deg,#f7b500 0 20px,#f28a00 20px 40px,#e52229 40px 60px,#c2207f 60px 80px,#7b3ea0 80px 100px,#2c77c2 100px 120px,#1aa6b7 120px 140px,#5cb531 140px 160px)}
.contact-tab{position:absolute;left:790px;top:0;width:130px;height:36px;background:#3a3a3a;border-radius:0 0 8px 8px;color:#fff;font:600 17px "Open Sans",sans-serif;text-align:center;line-height:38px}
.logo{position:absolute;left:42px;top:48px;font:600 43px/1 "Montserrat",sans-serif;color:var(--brand);letter-spacing:-1.5px}
.nav{position:absolute;left:44px;top:119px;display:flex;gap:33px;font:17.5px "Indie Flower",cursive;color:#555}
.nav .current{color:var(--link-red)}
.social{position:absolute;right:40px;top:120px;display:flex;gap:12px}
.social span{display:flex;align-items:center;gap:4px;font:700 10px/14px "Open Sans",sans-serif;color:var(--social)}
.social i{width:10px;height:10px;border-radius:50%;background:var(--social);display:block}
.nav-rule{position:absolute;left:42px;top:158px;width:878px;height:3px;background:var(--rule)}
.hero{position:absolute;left:42px;top:179px;width:878px;height:340px;background:
  radial-gradient(circle at 5% 50%,rgba(255,240,220,.55) 0,transparent 12%),
  radial-gradient(circle at 58% 30%,rgba(255,245,230,.5) 0,transparent 10%),
  radial-gradient(ellipse at 36% 35%,#a07a64 0,#6a4a3c 30%,transparent 60%),
  radial-gradient(ellipse at 85% 40%,#8a6a5a 0,transparent 45%),
  linear-gradient(90deg,#3a2822,#2a1e1a 60%,#4a3a34)}
.quote{position:absolute;left:470px;top:321px;width:450px;height:168px;background:rgba(25,20,18,.72);border-radius:8px 0 0 8px;padding:20px 26px 0 25px;color:#fff;font:italic 13.4px/18px "Noto Serif",serif}
.quote cite{display:block;text-align:right;margin-top:17px;font-weight:700;font-size:13.4px}
.carousel-arrow{position:absolute;top:580px;width:30px;height:40px;background:#111}
.carousel-arrow.prev{left:26px;border-radius:20px 0 0 20px}
.carousel-arrow.next{left:906px;border-radius:0 20px 20px 0}
.carousel-arrow svg{position:absolute;top:14px;left:0}
.thumb{position:absolute;top:540px;width:205px;height:120px;overflow:hidden}
.thumb .play{position:absolute;left:77px;top:36px;width:50px;height:48px;background:rgba(60,60,60,.55)}
.thumb .play svg{position:absolute;left:15px;top:12px}
.thumb .caption{position:absolute;left:0;bottom:0;width:100%;height:26px;background:rgba(0,0,0,.8);color:#fff;font:700 11px/27px "Open Sans",sans-serif;padding-left:9px;letter-spacing:.4px;white-space:nowrap}
.divider{position:absolute;left:42px;top:684px;width:878px;height:1px;background:linear-gradient(90deg,transparent,#777 15%,#777 85%,transparent)}
.welcome{position:absolute;left:60px;top:700px;width:540px}
.welcome h1{font:400 28px "Indie Flower",cursive;color:#333;margin-bottom:12px;letter-spacing:.3px}
.welcome p{font-size:10.6px;line-height:14px;color:var(--ink-soft);margin-bottom:14px;letter-spacing:.15px}
.welcome a{color:var(--link-red);text-decoration:none}
.new-videos{position:absolute;left:650px;top:706px;width:242px}
.new-videos h2{font:400 17px "Open Sans",sans-serif;color:#333}
.new-videos .all{position:absolute;right:0;top:7px;font-size:10px;color:var(--link-red)}
.video-grid{display:grid;grid-template-columns:110px 110px;column-gap:19px;row-gap:14px;margin-top:11px;margin-left:1px}
.video-card .shot{width:110px;height:77px;border-radius:7px}
.video-card .artist{font:700 12px/14px "Open Sans",sans-serif;color:var(--link-blue);margin-top:7px;letter-spacing:.4px}
.video-card .title{font:13.5px/18px "Open Sans",sans-serif;color:var(--link-navy)}
.footer{position:absolute;left:0;top:1017px;width:960px;height:63px;background:linear-gradient(#333,var(--footer))}
.footer nav{position:absolute;left:61px;top:17px;display:flex;gap:21px;font-size:11px;color:#fff}
.footer .copy{position:absolute;right:69px;top:17px;font-size:11px;color:var(--footer-text)}
</style>
</head>
<body>
<div class="page">
  <div class="rainbow"></div>
  <div class="contact-tab">contact us</div>
  <div class="logo">northgateclipworks</div>
  <nav class="nav">
    <span>Home</span><span class="current">Music Video</span><span>Promo Features</span><span>Band Site Design</span><span>Prices</span>
  </nav>
  <div class="social">
    <span><i></i>Friendly</span><span><i></i>Chirper</span><span><i></i>Pixora</span><span><i></i>Linkwork</span>
  </div>
  <div class="nav-rule"></div>

  <div class="hero" role="img" aria-label="Still from a music video: a singer performing at a vintage microphone under warm stage lights"></div>
  <blockquote class="quote">
    “I have a great working relationship with NCW and remain continually impressed with their professionalism throughout any of my projects. They have always delivered the goods and within budget. Would definitely work with these nice people again and happily recommend them to anybody....”
    <cite>True Echo (Recording Artist/LoudRoomCast)</cite>
  </blockquote>

  <div class="carousel-arrow prev"><svg width="30" height="12" viewBox="0 0 30 12"><path d="M19 0 L13 6 L19 12Z" fill="#fff"/></svg></div>
  <div class="thumb" style="left:60px;background:radial-gradient(ellipse at 50% 70%,#8a7e78 0,transparent 55%),linear-gradient(#2e2e2e,#4a4644)" role="img" aria-label="Showreel still: a figure lying in a dim room">
    <div class="play"><svg width="22" height="24"><path d="M0 0 L22 12 L0 24Z" fill="#ddd"/></svg></div>
    <div class="caption">Northgate Clip Works Showreel</div>
  </div>
  <div class="thumb" style="left:271px;background:radial-gradient(ellipse at 40% 40%,#7a9ad0 0,transparent 45%),linear-gradient(#142446,#2e4a80)" role="img" aria-label="Video still: a band on a blue-lit stage">
    <div class="play"><svg width="22" height="24"><path d="M0 0 L22 12 L0 24Z" fill="#ddd"/></svg></div>
    <div class="caption">MC Halden - "Escape"</div>
  </div>
  <div class="thumb" style="left:483px;background:radial-gradient(ellipse at 30% 20%,#eeeae6 0,transparent 50%),linear-gradient(#c8c4c0,#5a5350)" role="img" aria-label="Video still: people gathered around a boxing ring">
    <div class="play"><svg width="22" height="24"><path d="M0 0 L22 12 L0 24Z" fill="#ddd"/></svg></div>
    <div class="caption">Dara K - "I Loved You"</div>
  </div>
  <div class="thumb" style="left:697px;background:radial-gradient(ellipse at 20% 20%,#fbe6c8 0,transparent 45%),linear-gradient(180deg,#f0c08a 0,#d88a56 70%,#c02a22 100%)" role="img" aria-label="Video still: a performer in a warm-lit train carriage">
    <div class="play"><svg width="22" height="24"><path d="M0 0 L22 12 L0 24Z" fill="#ddd"/></svg></div>
  </div>
  <div class="carousel-arrow next"><svg width="30" height="12" viewBox="0 0 30 12"><path d="M11 0 L17 6 L11 12Z" fill="#fff"/></svg></div>

  <div class="divider"></div>

  <section class="welcome">
    <h1>Welcome to NorthgateClipWorks.example</h1>
    <p>We're a London based music video production company that specialise in affordable band promo and music video production - whether it's for unsigned artists, specialist performers or large record labels - no matter what the genre or style of your music/performance, we can help you promote it!</p>
    <p>Our music videos have been broadcast on Vidwave, Vidwave Beat, Vidwave Europa, The Crate, Channel Q, The Chart Channel, Homereel Vmx Street, to name a few.</p>
    <p>For more information, advice or to chat about what you have in mind for your next music video call Maren on 07700 900 418 - or drop us a quick email, we're always happy to help or offer advice for free.</p>
    <p>Email: <a href="#">info@northgateclipworks.example</a></p>
  </section>

  <section class="new-videos">
    <h2>New Videos</h2>
    <span class="all">All videos &gt;</span>
    <div class="video-grid">
      <div class="video-card"><div class="shot" style="background:radial-gradient(ellipse at 50% 55%,#6a4634 0,#2a1c16 45%,#0e0e0e 80%)" role="img" aria-label="Video still: smiling artist on a black background"></div><div class="artist">D Kavi Marlow</div><div class="title">Break This Game</div></div>
      <div class="video-card"><div class="shot" style="background:radial-gradient(ellipse at 40% 40%,#b09a84 0,#5a4a3c 45%,#2a221c 90%)" role="img" aria-label="Video still: crowd scene with performers"></div><div class="artist">MC Halden</div><div class="title">Grenade</div></div>
      <div class="video-card"><div class="shot" style="background:radial-gradient(ellipse at 50% 40%,#f0c8a4 0,#c88a62 50%,#7a4a30 100%)" role="img" aria-label="Video still: close-up portrait in warm light"></div><div class="artist">D Kavi Marlow</div><div class="title">Break This Game</div></div>
      <div class="video-card"><div class="shot" style="background:radial-gradient(ellipse at 50% 60%,#6a3a48 0,#2a1a20 50%,#0c0c0c 90%)" role="img" aria-label="Video still: group of performers on a dark stage"></div><div class="artist">MC Halden</div><div class="title">Grenade</div></div>
    </div>
  </section>

  <footer class="footer">
    <nav><span>Terms &amp; Conditions</span><span>Privacy Policy</span><span>Site Map</span></nav>
    <div class="copy">Copyright © 2011, Northgate Clip Works</div>
  </footer>
</div>
</body>
</html>
```